Orthopedic Arm Surgeon Brochure

Bifold modern design. I will supply the text, my photo, and photos of my textbooks. Prefer colors in the greens, blues, greys. For more information visit LimbForwardClinic.com Please feel free to e-mail me with any questions. Current brochure attached; I want to modernize this, get rid of frames, and change the text.

Target Market(s)

High-end market

Colors
3176b5
33a6d7
33b8a4
abd036
876aae
b768aa

Requirements
Must have
• Beautiful finishes
Should not have
• Bright reds, yellows, oranges that emit fear

```html
<!DOCTYPE html>
<html lang="en">
<head>
<meta charset="utf-8">
<title>Orthopedic Arm Surgeon Brochure</title>
<link rel="stylesheet" href="https://fonts.googleapis.com/css2?family=Open+Sans:ital,wght@0,400;0,600;0,700;1,400&family=Cinzel:wght@400;600&family=Oswald:wght@400;500&family=Noto+Serif:wght@400;700&display=swap">
<style>
:root{
  --backdrop:#8a5a36;
  --blue:#2f74bd;
  --blue-light:#3d86cc;
  --teal:#2cb3a0;
  --lime:#abd036;
  --green-dark:#1f5f2a;
  --grey-band:#dcd8cf;
  --paper:#f1f1f2;
  --ink:#3b3b3b;
  --heading-blue:#2f7cbf;
  --white:#ffffff;
}
*{box-sizing:border-box;margin:0;padding:0}
html,body{width:922px;height:1200px;overflow:hidden;background:var(--backdrop)}
body{font-family:"Open Sans",Arial,sans-serif;color:var(--ink)}
.canvas{position:relative;width:922px;height:1200px}
.abs{position:absolute}
.spread-label{position:absolute;color:#fff;font-size:15px;font-family:"Open Sans",sans-serif}
.spread{position:absolute;left:43px;width:810px;box-shadow:3px 4px 8px rgba(0,0,0,.35);overflow:hidden;background:var(--paper)}
.spread-outside{top:74px;height:528px}
.spread-inside{top:621px;height:528px}
.photo{position:absolute;border:2px solid #fff}
.blue-field{position:absolute;top:0;height:260px;background:linear-gradient(135deg,var(--blue) 0%,var(--blue-light) 55%,var(--blue) 100%)}
.grey-band{position:absolute;top:260px;height:124px;background:var(--grey-band)}
.doctor-name{position:absolute;color:#fff;font-weight:700;font-size:14px;text-align:center;width:405px}
.bio{position:absolute;left:48px;top:70px;width:310px;color:#fff;font-size:6.3px;line-height:11px;text-align:justify}
.books-box{position:absolute;left:29px;top:138px;width:358px;height:106px;background:var(--teal)}
.books-box p{color:#fff;font-style:italic;font-size:7.8px;line-height:13px;text-align:center;padding:7px 10px 0}
.book{position:absolute;top:40px;width:47px;height:60px}
.phone{position:absolute;font-family:"Oswald",sans-serif;font-weight:500;letter-spacing:1px;color:#2b2b2b}
.url-small{position:absolute;font-family:"Noto Serif",serif;font-size:6.3px;letter-spacing:2.4px;color:#666}
.brand{position:absolute;width:405px;display:flex;justify-content:center;align-items:center;gap:7px;color:var(--green-dark);font-family:"Open Sans",sans-serif;font-weight:700;font-size:15px;line-height:18px}
.brand-dot{width:12px;height:12px;border-radius:50%;background:var(--green-dark)}
.loc-bar{position:absolute;left:29px;top:450px;width:358px;height:15px;background:var(--teal);color:#fff;font-family:"Noto Serif",serif;font-weight:700;font-size:7.5px;line-height:15px;text-align:center}
.loc{position:absolute;top:473px;font-size:5.6px;line-height:8px;color:#222}
.loc h4{font-weight:400;font-size:6.8px;color:var(--green-dark);margin-bottom:4px}
.portrait{position:absolute;border-radius:50%;border:3px solid #fff;background:radial-gradient(circle at 50% 40%,#c9a58c,#5a5f6a 70%)}
.creds{position:absolute;left:405px;top:134px;width:405px;text-align:center;color:#fff;font-size:6.2px;line-height:9px}
.icon{position:absolute;top:180px;width:54px;height:54px;border-radius:50%;border:2px solid #e8eef6;background:radial-gradient(circle at 55% 50%,#e57f6b 0%,#e8c3ae 45%,#f4ece6 80%)}
.icon-label{position:absolute;top:238px;color:#fff;font-size:6px;width:80px;text-align:center}
.spec-title{position:absolute;left:405px;top:266px;width:405px;text-align:center;font-family:"Noto Serif",serif;font-weight:700;font-size:12.3px;letter-spacing:.5px;color:#333}
.spec-photo{position:absolute;top:285px;height:82px;background:linear-gradient(135deg,#efe2d8,#d89a82 55%,#c95e4d)}
.spec-label{position:absolute;top:371px;font-family:"Noto Serif",serif;font-weight:700;font-size:6.5px;color:#444;text-align:center}
.appt-pill{position:absolute;left:466px;top:478px;width:272px;height:12px;border-radius:6px;background:var(--lime);color:#fff;font-family:"Noto Serif",serif;font-weight:700;font-size:6.8px;line-height:12px;text-align:center;letter-spacing:.5px}
.url-large{position:absolute;font-family:"Noto Serif",serif;font-weight:700;color:var(--heading-blue);letter-spacing:1px}
.wrist-col{position:absolute;left:0;top:0;width:171px;height:351px;background:var(--teal);color:#fff;padding:30px 12px 0 28px}
.section-title{font-family:"Cinzel",serif;font-weight:600;font-size:14px;line-height:16px;color:var(--heading-blue);margin-bottom:12px}
.wrist-col .section-title{color:#fff}
.body-copy{font-size:5.3px;line-height:8.4px;text-align:justify}
.body-copy p{margin-bottom:6px}
.text-col{position:absolute;top:30px}
.lime-band{position:absolute;left:0;top:351px;width:810px;height:28px;background:var(--lime)}
.strip{position:absolute;top:387px;height:118px}
.footer-grey{position:absolute;left:0;top:505px;width:810px;height:23px;background:var(--grey-band)}
</style>
</head>
<body>
<div class="canvas">

<div class="spread-label" style="left:205px;top:40px">Back Cover</div>
<div class="spread-label" style="left:607px;top:40px">Front Cover</div>

<section class="spread spread-outside">
  <!-- back cover -->
  <div class="blue-field" style="left:0;width:405px"></div>
  <div class="grey-band" style="left:0;width:405px"></div>
  <h2 class="doctor-name" style="left:0;top:28px">Dr. Martin L. Harrow, MD</h2>
  <p class="bio">Dr. Harrow graduated Cum Laude from Eastbrook University and with honors from Weston Medical College. He completed his residency in Orthopaedic Surgery at the University of Pacifica. In order to obtain expertise covering the entire upper extremity, he completed two fellowships, one in Hand Surgery and the other in Sports Medicine. He is board certified in Orthopaedic Surgery and has a Certificate of Additional Qualification in Hand Surgery.</p>
  <div class="books-box">
    <p>Dr. Harrow is a nationally-recognized Upper Extremity Surgeon who has edited 7 textbooks, published over 4 original research papers and written 23 textbook chapters.</p>
    <div class="book" role="img" aria-label="Textbook cover" style="left:5px;background:linear-gradient(#6b4a2a,#b08a4a)"></div>
    <div class="book" role="img" aria-label="Textbook cover" style="left:56px;background:linear-gradient(#dfe3ea,#8a4a3a)"></div>
    <div class="book" role="img" aria-label="Textbook cover" style="left:107px;background:linear-gradient(#2a2550,#6a3a6a)"></div>
    <div class="book" role="img" aria-label="Textbook cover" style="left:158px;background:linear-gradient(#b9a27a,#6a2a20)"></div>
    <div class="book" role="img" aria-label="Textbook cover" style="left:209px;background:linear-gradient(#2d8ad0,#9ccbee)"></div>
    <div class="book" role="img" aria-label="Textbook cover" style="left:260px;background:linear-gradient(#a0182a,#d24a4a)"></div>
    <div class="book" role="img" aria-label="Textbook cover" style="left:311px;width:42px;background:linear-gradient(#d28a2a,#3a2a2a)"></div>
  </div>
  <div class="phone" style="left:0;width:405px;text-align:center;top:262px;font-size:16px">713-555-0148</div>
  <div class="photo" role="img" aria-label="Tennis player serving" style="left:29px;top:285px;width:77px;height:82px;background:linear-gradient(#8fc0e6,#3a7a3a)"></div>
  <div class="photo" role="img" aria-label="Football player with ball" style="left:111px;top:285px;width:87px;height:82px;background:linear-gradient(#6aa04a,#3a4a8a)"></div>
  <div class="photo" role="img" aria-label="Hand with wrist pain" style="left:203px;top:285px;width:88px;height:82px;background:linear-gradient(135deg,#eee0d4,#c9a08a)"></div>
  <div class="photo" role="img" aria-label="Person holding painful elbow" style="left:296px;top:285px;width:89px;height:82px;background:linear-gradient(135deg,#bfc6cc,#d9b9a4)"></div>
  <div class="url-small" style="left:0;width:405px;text-align:center;top:371px">www.LimbForwardClinic.com</div>
  <div class="brand" style="left:0;top:410px"><span class="brand-dot"></span><span>Alderbrook Limb Care</span></div>
  <div class="loc-bar">Dr. Harrow sees patients at the following locations:</div>
  <div class="loc" style="left:29px"><h4>MEDICAL DISTRICT</h4>4210 Linden Street,<br>Suite 300, Houston,<br>Texas 77030</div>
  <div class="loc" style="left:132px;padding-left:6px;border-left:1px solid #aaa"><h4>PEARLAND</h4>2250 Harbor Oak Dr<br>Suite 110, Pearland,<br>Texas 77584</div>
  <div class="loc" style="left:231px;padding-left:6px;border-left:1px solid #aaa"><h4>KATY</h4>318 Cedar Hollow Dr<br>Katy,<br>Texas 77450</div>
  <div class="loc" style="left:306px;padding-left:6px;border-left:1px solid #aaa"><h4>CYFAIR</h4>9820 Meadow Ridge Rd<br>Houston,<br>Texas 77065</div>

  <!-- front cover -->
  <div class="blue-field" style="left:405px;width:405px"></div>
  <div class="grey-band" style="left:405px;width:405px"></div>
  <div class="portrait" role="img" aria-label="Portrait of the surgeon" style="left:566px;top:28px;width:74px;height:74px"></div>
  <h1 class="doctor-name" style="left:405px;top:108px">Dr. Martin L. Harrow, MD</h1>
  <p class="creds">Board Certified Orthopedic Surgeon<br>Certificate of Additional Qualification, Hand Surgery</p>
  <div class="icon" role="img" aria-label="Carpal tunnel" style="left:425px"></div>
  <div class="icon" role="img" aria-label="Cubital tunnel" style="left:485px"></div>
  <div class="icon" role="img" aria-label="Trigger finger" style="left:546px"></div>
  <div class="icon" role="img" aria-label="De Quervain's tendinitis" style="left:610px"></div>
  <div class="icon" role="img" aria-label="Elbow pain" style="left:670px"></div>
  <div class="icon" role="img" aria-label="Shoulder pain" style="left:727px"></div>
  <div class="icon-label" style="left:412px">Carpal tunnel</div>
  <div class="icon-label" style="left:472px">Cubital Tunnel</div>
  <div class="icon-label" style="left:533px">Trigger Finger</div>
  <div class="icon-label" style="left:592px;width:90px">De Quervain's tendinitis</div>
  <div class="icon-label" style="left:667px;width:60px">Elbow Pain</div>
  <div class="icon-label" style="left:714px">Shoulder Pain</div>
  <div class="spec-title">SPECIALIST IN SURGERY OF</div>
  <div class="spec-photo photo" role="img" aria-label="Shoulder pain" style="left:423px;width:90px"></div>
  <div class="spec-photo photo" role="img" aria-label="Hand pain" style="left:519px;width:90px"></div>
  <div class="spec-photo photo" role="img" aria-label="Elbow pain" style="left:615px;width:78px"></div>
  <div class="spec-photo photo" role="img" aria-label="Wrist pain" style="left:699px;width:90px"></div>
  <div class="spec-label" style="left:423px;width:90px">SHOULDER</div>
  <div class="spec-label" style="left:519px;width:90px">HAND</div>
  <div class="spec-label" style="left:615px;width:78px">ELBOW</div>
  <div class="spec-label" style="left:699px;width:90px">WRIST</div>
  <div class="brand" style="left:405px;top:410px"><span class="brand-dot"></span><span>Alderbrook Limb Care</span></div>
  <div class="phone" style="left:405px;width:405px;text-align:center;top:452px;font-size:17px;color:#444">713-555-0148</div>
  <div class="appt-pill">APPOINTMENTS CAN BE MADE ONLINE THROUGH: BOOKCARE.COM</div>
  <div class="url-large" style="left:405px;width:405px;text-align:center;top:495px;font-size:15px">www.LimbForwardClinic.com</div>
</section>

<section class="spread spread-inside">
  <div class="wrist-col">
    <h2 class="section-title">Wrist Pain</h2>
    <div class="body-copy">
      <p>Wrist pain may have many causes and the diagnosis is best made by a fellowship-trained Hand Surgeon. The most common cause is DeQuervain's tendinitis, which causes pain on the thumb side of the wrist. This occurs when the tendons to the thumb and wrist get pinched in their tunnel. Pain is usually worse with lifting and gripping.</p>
      <p>DeQuervain's Tendinitis is common in mothers who repetitively lift children. It can also occur following frequent lifting with the thumb up, such as when pulling weeds, luggage or moving heavy objects.</p>
      <p>Initial treatment is to avoid lifting with the thumb up. If lifting is necessary, lift with the palm up or the palm down. To lift small children, keep the palm up and 'scoop under' the child. A single steroid injection often helps by decreasing inflammation in the tunnel. In mild cases, this can be curative, especially if the problem is treated early and stressful activities can be avoided. Sometimes there's a very small second tunnel that causes problems and doesn't respond well to injections.</p>
      <p>If the tendinitis recurs after injection, an outpatient tendon release is very effective. To prevent tendon subluxation after tunnel release, I lengthen the restraints that stabilize the tendon and repair them in a lengthened position. To see a video of a DeQuervain's Tendinitis Release please go to: www.LimbForwardClinic.com</p>
    </div>
  </div>
  <div class="text-col" style="left:186px;width:201px">
    <h2 class="section-title">Carpal Tunnel Syndrome</h2>
    <div class="body-copy">
      <p>Carpal Tunnel Syndrome occurs when the median nerve to the hand gets pinched at the wrist. This leads to fingers feeling "numb", "asleep", "cold", like they "lack circulation" or have "pins and needles" in them. Carpal tunnel syndrome is usually worst at night or upon awakening. If you wake up at night with your hand numb or painfully asleep, and have to "shake it out" to get relief, you've probably got carpal tunnel syndrome. Symptoms also often occur with gripping, such as when driving, writing or holding books, cell phones or tools.</p>
      <p>Unless the carpal tunnel syndrome has led to nerve damage, initial treatment often involves splinting the wrist at night when asleep. If that doesn't work, the carpal tunnel can be released. The least invasive technique is the Single-Incision Endoscopic Carpal Tunnel Release. This quick, minimally invasive, outpatient procedure uses a small incision at the wrist without any incision in the hand. Compared to other techniques, there is decreased pain and a quicker return to work and other activities. There are no bandages, and hand washing and showering can be performed immediately. To see a video of an Endoscopic Carpal Tunnel Release please go to: www.LimbForwardClinic.com</p>
    </div>
  </div>
  <div class="abs" role="img" aria-label="Hand with glowing wrist pain" style="left:187px;top:227px;width:199px;height:110px;background:radial-gradient(circle at 42% 48%,#e2554a 0%,#e9c3b3 22%,#dcdcdc 60%,#c9c9c9)"></div>

  <div class="text-col" style="left:423px;width:180px">
    <h2 class="section-title">Cubital Tunnel Syndrome</h2>
    <div class="body-copy">
      <p>Cubital tunnel syndrome occurs when the funny bone (ulnar) nerve gets pinched at the elbow. This leads to tingling and numbness of the small finger when the elbow is bent, usually at night or when talking on the phone. Numbness may also occur when the elbows is placed on a hard surface.</p>
      <p>Unless nerve damage has occurred, treatment starts with avoiding pressure on the elbow, and not resting the elbow on desks, arm rests, or other hard objects. Avoid prolonged elbow flexion: use the other hand to hold phones or get a hands-free device.</p>
      <p>If this fails, the least invasive definitive treatment is an Endoscopic Cubital Tunnel Release. This minimally invasive, outpatient procedure allows an early return to activities with a low complication rate. No splint is used after surgery. To see a video of an Endoscopic Cubital Tunnel Release please go to: www.LimbForwardClinic.com</p>
    </div>
  </div>
  <div class="text-col" style="left:615px;width:167px">
    <h2 class="section-title">Trigger Finger</h2>
    <div class="body-copy">
      <p>Trigger finger occurs when the tendon that moves the finger gets pinched in its tunnel. This causes the finger to get stuck or stiff, which is often worse in the morning. This catching or locking can be quite painful. Grip may also cause pain. The finger may occasionally get stuck straight and be difficult to bend.</p>
      <p>Splinting may temporarily prevent the catching, but doesn't actually treat the problem. If caught early, a steroid injection can be curative. After 4-6 months the chance of an injection permanently curing the condition is lower, but still often worth a try.</p>
      <p>If the triggering returns following an injection, the problem can be definitively treated with a minimally-invasive Trigger Finger Release. This highly successful outpatient surgery is almost always a permanent cure. To see a video of a Trigger Finger Release please go to:</p>
    </div>
  </div>
  <div class="photo" role="img" aria-label="Portrait of the surgeon" style="left:565px;top:235px;width:77px;height:79px;border-width:3px;background:linear-gradient(#e9e9ea,#3b3f48)"></div>
  <div class="abs" style="left:423px;top:319px;width:360px;height:1px;background:#cfcfcf"></div>
  <div class="abs" style="left:432px;top:325px;font-family:'Noto Serif',serif;font-size:8px;letter-spacing:.6px;color:#555">APPOINTMENTS CAN BE MADE ONLINE THROUGH: <b style="font-size:12px;color:var(--green-dark)">BOOKCARE.COM</b></div>

  <div class="lime-band"></div>
  <div class="abs" style="left:195px;top:355px;color:#fff;font-family:'Noto Serif',serif;font-size:13px">Call: <b style="font-size:17px;letter-spacing:1.5px">713-555-0148</b></div>
  <div class="url-large" style="left:467px;top:356px;font-size:14.5px;color:#fff;letter-spacing:1.5px">www.LimbForwardClinic.com</div>

  <div class="strip" role="img" aria-label="Cyclist holding injured shoulder" style="left:0;width:136px;background:linear-gradient(135deg,#6aa85a,#c2504a 60%,#2a2a2a)"></div>
  <div class="strip" role="img" aria-label="Golfer with painful wrist" style="left:137px;width:158px;background:linear-gradient(135deg,#3a7ad0,#e5e5e5 60%,#6aa04a)"></div>
  <div class="strip" role="img" aria-label="Tennis player with elbow pain" style="left:296px;width:90px;background:linear-gradient(#8cc0e8,#d9b8a0 60%,#f0f0f0)"></div>
  <div class="strip" role="img" aria-label="Man holding painful elbow" style="left:387px;width:105px;background:linear-gradient(135deg,#3a3f46,#b07e62)"></div>
  <div class="strip" role="img" aria-label="Woman's bare shoulder" style="left:493px;width:127px;background:linear-gradient(135deg,#f4f1ee,#e2c3ae)"></div>
  <div class="strip" role="img" aria-label="Arm with highlighted elbow pain" style="left:621px;width:100px;background:linear-gradient(135deg,#e9e9e9,#d9a084 50%,#d8453c)"></div>
  <div class="strip" role="img" aria-label="Back view of shoulder pain" style="left:722px;width:88px;background:linear-gradient(135deg,#b85a3e,#e2a584)"></div>
  <div class="footer-grey"></div>
</section>

<div class="spread-label" style="left:194px;top:1157px">Front Inside</div>
<div class="spread-label" style="left:595px;top:1157px">Back inside</div>

</div>
</body>
</html>
```